Wordpress Identity for Innovation Firm

Copper Lantern Partners is an innovation and investment firm based in Los Angeles.

We are seeking a designer that can help create our company identity and Wordpress site.

The attached Design Brief provides more details.

Designers Responsibility:

1) Company Identity

The designer will create the company identity.
Attached is a file that contains a type font that I like a lot.
No logo design is required.

The Copper Lantern Partners type font should become the company identity.
The attached document provides an overview of company type font identities that we like.

2) Wordpress Theme & Design

The designer will select existing Wordpress Themes that meet our design desires, and present them as part of the design proposal.

We will make our selection based on the selected Wordpress Theme(s), which the designer will creatively adapt with the new company identity.

Target Market(s)

We anticipate the website being mostly accessed by the US, Canada and European countries.

Our target audience includes the following:

• Corporations, companies, startups, non-profits
• Banks, venture capital, private equity, investors
• Incubators, accelerators, innovation clusters, research labs, universities
• Ad agencies, marketing agencies, digital agencies, media, press

Industry/Entity Type

Investment

Number of Pages Required

1 page

Font styles to use
Sans Serif
Other font styles liked:
• See attached design brief materials. The Font will represent the brand identity!

Requirements
Must have
• The ability to scroll through information top to bottom is important to us.
• This is in line with today's Wordpress themes.
• The website must be able to function across devices (desktop, tablet, phone).
• The top 5 web browsers and platforms (Mac/PC/Android/iOS)
• Contact us link or information field
Nice to have
• It would be nice to have a moving image in the background, such as:
• https://drifttrial.sitehatch.com
• The Wordpress theme of the moving image or video should be relevant to our overall Technology Innovation theme.
• Key words:
• Technology Innovation
• Digital
• Business
• Transportation
• Advanced Vehicles (auto, boat, airplane, rail, space)
• Space
• Venture Capital
• Investing
Should not have
• eCommerce

```html
<!DOCTYPE html>
<html lang="en">
<head>
<meta charset="utf-8">
<title>Copper Lantern Partners</title>
<link rel="stylesheet" href="https://fonts.googleapis.com/css2?family=Open+Sans:wght@300;400;600;700;800&display=swap">
<style>
:root{
  --ink:#1d1d1d;
  --black:#111;
  --grey:#8a8a8a;
  --light:#b9b9b9;
  --text:#555;
  --white:#fff;
  --footer:#2a2a2a;
  --footer-dark:#1e1e1e;
  --footer-text:#9a9a9a;
  --label:#444;
}
*{margin:0;padding:0;box-sizing:border-box}
html,body{width:1200px;height:2400px;overflow:hidden;background:#f4f4f4}
body{font-family:"Open Sans",Arial,sans-serif;color:var(--text);position:relative}
.page{position:absolute;inset:0;background:var(--white)}

/* hero */
.hero{position:absolute;left:0;top:0;width:1200px;height:560px}
.hero-photo{position:absolute;inset:0;background:linear-gradient(100deg,#6d7277 0%,#b7b9ba 35%,#d9d8d4 55%,#8f8b85 80%,#4f4c48 100%)}
.hero-shade{position:absolute;inset:0;background:linear-gradient(90deg,rgba(0,0,0,.45),rgba(0,0,0,.05) 60%)}
.topbar{position:absolute;left:0;top:0;width:100%;height:86px;background:rgba(20,20,20,.55)}
.brand-name{position:absolute;left:40px;top:26px;font-size:30px;font-weight:600;color:var(--white)}
.utility{position:absolute;right:40px;top:12px;display:flex;gap:10px;align-items:center;font-size:12px;color:var(--white)}
.dot{width:12px;height:12px;border-radius:50%;background:var(--white);opacity:.85}
.nav{position:absolute;right:40px;top:50px;display:flex;gap:20px;font-size:13px;font-weight:600;color:var(--white)}
.mission{position:absolute;left:30px;top:300px;width:560px;color:var(--white)}
.mission h1{font-size:38px;font-weight:800;letter-spacing:1px;margin-bottom:12px}
.mission p{font-size:19px;font-weight:600;line-height:1.35;margin-bottom:18px}
.btn-dark{display:inline-block;background:var(--black);color:var(--white);font-size:12px;font-weight:700;padding:8px 14px;letter-spacing:.5px}

/* intro */
.intro{position:absolute;left:60px;top:610px;width:1080px;font-size:44px;font-weight:300;line-height:1.15;color:var(--light)}
.intro strong{font-weight:300;color:var(--grey)}

/* services */
.services{position:absolute;left:60px;top:890px;width:1080px;display:flex;gap:20px}
.service{width:255px}
.service-photo{height:150px;background:linear-gradient(135deg,#9aa0a5,#d2d0cb 55%,#6e6a64)}
.service-title{height:120px;background:var(--black);color:var(--white);font-size:19px;font-weight:700;line-height:1.25;padding:16px 14px}
.service p{font-size:14px;line-height:1.55;color:var(--text);margin:14px 0 14px}
.read{font-size:14px;color:var(--ink);font-weight:600}

/* brand band */
.brand-band{position:absolute;left:0;top:1420px;width:1200px;height:120px;background:var(--black);overflow:hidden}
.brand-band h2{position:absolute;left:60px;top:8px;font-size:118px;font-weight:800;color:var(--white);letter-spacing:4px;line-height:1}
.btn-outline{position:absolute;right:60px;top:1540px;border:1px solid var(--ink);background:var(--white);font-size:13px;font-weight:700;color:var(--ink);padding:9px 30px;letter-spacing:.5px}
.partners{position:absolute;left:40px;top:1610px;width:1120px;height:80px;display:flex;align-items:center;justify-content:space-between}
.partner-name{font-size:22px;font-weight:600;letter-spacing:2px;color:var(--label)}
.arrow{width:22px;height:40px}

/* identity card */
.card{position:absolute;left:440px;top:1770px;width:340px;height:210px;background:var(--white);box-shadow:0 6px 18px rgba(0,0,0,.18);padding:44px 30px}
.card strong{display:block;font-size:18px;font-weight:700;color:var(--ink)}
.card small{font-size:12px;color:var(--grey)}

/* footer */
.newsletter{position:absolute;left:0;top:2060px;width:1200px;height:70px;background:var(--footer-dark);display:flex;align-items:center;padding:0 60px}
.newsletter h3{font-size:24px;font-weight:700;color:var(--white);margin-right:24px}
.newsletter p{font-size:12px;color:var(--footer-text);width:240px;line-height:1.4}
.field{margin-left:auto;width:400px;height:34px;background:#3b3b3b;color:var(--footer-text);font-size:12px;padding:9px 14px}
.subscribe{height:34px;background:#555;color:var(--white);font-size:13px;font-weight:700;padding:8px 18px}
.footer{position:absolute;left:0;top:2130px;width:1200px;height:220px;background:var(--footer);display:flex;gap:70px;padding:24px 60px}
.footer-col h4{font-size:13px;font-weight:700;color:var(--white);margin-bottom:12px}
.footer-col li{list-style:none;font-size:12px;color:var(--footer-text);line-height:1.7}
.footer-col.news{width:230px}
.news li{margin-bottom:8px;line-height:1.4}
.social{display:flex;gap:14px}
.social .dot{width:20px;height:20px;background:var(--footer-text)}
.bottom{position:absolute;left:0;top:2350px;width:1200px;height:50px;background:var(--footer-dark);color:var(--footer-text);font-size:12px;text-align:center;line-height:50px}
</style>
</head>
<body>
<div class="page">
  <section class="hero">
    <div class="hero-photo" role="img" aria-label="Business team meeting around a table"></div>
    <div class="hero-shade"></div>
    <header class="topbar">
      <div class="brand-name">Copper Lantern Partners</div>
      <div class="utility"><span class="dot"></span><span class="dot"></span><span class="dot"></span><span>contact@copperlantern.com</span></div>
      <nav class="nav"><span>HOME</span><span>ABOUT</span><span>WORK</span><span>NEWS</span><span>CONTACT</span></nav>
    </header>
    <div class="mission">
      <h1>OUR MISSION</h1>
      <p>Copper Lantern Partners' mission is to create sustainable competitive advantage through superior innovation and operating performance and the ability to provide de-risked partnership models.</p>
      <span class="btn-dark">READ MORE</span>
    </div>
  </section>

  <p class="intro"><strong>Copper Lantern Partners</strong> is an innovation and investment firm, which creates sustainable competitive advantage through de-risked partnership models and superior operating performance.</p>

  <section class="services">
    <article class="service">
      <div class="service-photo" role="img" aria-label="Team of colleagues posing together"></div>
      <h3 class="service-title">We transform business challenges into significant growth platforms</h3>
      <p>Today's age of innovation is driven by the accelerating evolution of technology and data, which has fundamentally changed consumer behavior. As a result, companies are faced with unrelenting pressure to put innovation at the center of their business.</p>
      <span class="read">Read more →</span>
    </article>
    <article class="service">
      <div class="service-photo" role="img" aria-label="Partners shaking hands in an office"></div>
      <h3 class="service-title">We partner with companies to develop new businesses</h3>
      <p>Copper Lantern Partners introduces new ways of thinking and doing in order to create gains in changing competitive environments. Most large companies are structured to maximize efficiency, minimize variances and avoid experimentation.</p>
      <span class="read">Read more →</span>
    </article>
    <article class="service">
      <div class="service-photo" role="img" aria-label="Colleagues collaborating at laptops"></div>
      <h3 class="service-title">Collaboration</h3>
      <p>Copper Lantern Partners cultivates radical collaboration by building businesses and taking complex technological challenges — not just generating ideas. Our key goal is to drive growth for our partners and support them to stay relevant in the digital era.</p>
      <span class="read">Read more →</span>
    </article>
    <article class="service">
      <div class="service-photo" role="img" aria-label="Presenter speaking to a small group"></div>
      <h3 class="service-title">Outcomes</h3>
      <p>Copper Lantern Partners is an entrepreneurial organization that cares about outcomes. We fundamentally believe that the greatest success in innovation originates from entrepreneurs — not consultants.</p>
      <span class="read">Read more →</span>
    </article>
  </section>

  <section class="brand-band"><h2>BRAND</h2></section>
  <span class="btn-outline">VIEW MORE BRAND</span>
  <div class="partners">
    <svg class="arrow" viewBox="0 0 22 40"><path d="M18 2 4 20l14 18" fill="none" stroke="#1d1d1d" stroke-width="2"/></svg>
    <span class="partner-name">VELLOR</span>
    <span class="partner-name">MARIN CASTELL</span>
    <span class="partner-name">ELVA</span>
    <span class="partner-name">ORVANE</span>
    <span class="partner-name">SOLENE</span>
    <span class="partner-name">MIREE</span>
    <svg class="arrow" viewBox="0 0 22 40"><path d="M4 2l14 18L4 38" fill="none" stroke="#1d1d1d" stroke-width="2"/></svg>
  </div>

  <div class="card">
    <strong>Copper Lantern Partners</strong>
    <small>seeking our unique identity</small>
  </div>

  <section class="newsletter">
    <h3>NEWSLETTER</h3>
    <p>Sign up to receive our latest news and updates about our firm directly to your inbox.</p>
    <span class="field">Stay up to date with our latest news</span>
    <span class="subscribe">SUBSCRIBE</span>
  </section>
  <footer class="footer">
    <div class="footer-col"><h4>QUICK LINKS</h4><ul><li>Home</li><li>About</li><li>Work</li><li>News</li><li>Contact</li></ul></div>
    <div class="footer-col news"><h4>RECENT NEWS</h4><ul><li>June 10, 2015 · 2 min<br>Our team joins a new innovation cluster</li><li>June 02, 2015 · 3 min<br>New partnership model launched this month</li></ul></div>
    <div class="footer-col"><h4>FOLLOW US</h4><div class="social"><span class="dot"></span><span class="dot"></span><span class="dot"></span></div></div>
    <div class="footer-col"><h4>CONTACT US</h4><ul><li>100 Harbor Lane, Suite 4</li><li>Los Angeles, CA</li><li>(555) 010-0427</li><li>contact@copperlantern.com</li></ul></div>
  </footer>
  <div class="bottom">© 2015 Copper Lantern Partners · Terms and Conditions · Privacy Policy · Terms of Use</div>
</div>
</body>
</html>
```